American cannabis tech company business card design

Quillo.com is seeking a modern, professional, and brand-aligned business card that represents our company and its core values: Mission, Story, Values, and Impact. As an innovative cannabis company, we want a business card that is not only visually appealing but also serves as a representation of who we are and what we stand for.

Project Scope: Design a double-sided business card that integrates our brand identity and core values. Incorporate our key brand elements, ensuring a sleek and contemporary aesthetic. Visually reflect our core values (Mission, Story, Values, Impact) in a way that is engaging yet professional.

Target Market(s)

Vendors, third parties,

Contact Information for Business Card

Contact details (name, title, email, phone, website, etc.)

Font styles to use
Other font styles liked:
• Caslon, Centra

Colors

Designer to choose colors to be used in the design.

Requirements
Must have
• Quillo.com logo and branding A creative yet clean way to integrate our core values (Mission, Story, Values, Impact) Modern typography and a well-structured layout
Nice to have
• forest green, grey, white, black
Should not have
• references to marijuana, leafs, plants, or related product

```html
<!DOCTYPE html>
<html lang="en">
<head>
<meta charset="utf-8">
<title>Quillo.com Business Card</title>
<link href="https://fonts.googleapis.com/css2?family=Montserrat:wght@400;700&family=Lato:wght@400&display=swap" rel="stylesheet">
<style>
  :root {
    --forest: #1b3220;
    --forest-light: #6f9a78;
    --forest-ink: #1d3a22;
    --paper: #ffffff;
    --ink: #1a1a1a;
    --grey: #55605a;
    --rule: #8a9a8e;
    --backdrop: #e9ebea;
  }
  * { margin: 0; padding: 0; box-sizing: border-box; }
  html, body {
    width: 1200px;
    height: 900px;
    overflow: hidden;
    background: var(--backdrop);
  }
  .canvas {
    width: 1200px;
    height: 900px;
    display: flex;
    flex-direction: column;
    align-items: center;
    justify-content: center;
    gap: 40px;
  }
  .card {
    width: 620px;
    height: 354px;
    border-radius: 22px;
    position: relative;
    box-shadow: 0 10px 30px rgba(0,0,0,0.12);
  }
  .card-front {
    background: var(--forest);
    display: flex;
    align-items: center;
    justify-content: center;
  }
  .brand-name {
    font-family: "Montserrat", sans-serif;
    font-weight: 700;
    font-size: 88px;
    letter-spacing: 2px;
    color: var(--forest-light);
    line-height: 1;
  }
  .card-back {
    background: var(--paper);
    display: flex;
    align-items: center;
    justify-content: center;
    gap: 44px;
    padding-top: 70px;
  }
  .identity { text-align: right; }
  .person-name {
    font-family: "Montserrat", sans-serif;
    font-weight: 700;
    font-size: 26px;
    color: var(--forest-ink);
    line-height: 1.1;
  }
  .person-title {
    font-family: "Montserrat", sans-serif;
    font-weight: 400;
    font-size: 15px;
    color: var(--grey);
    margin-top: 2px;
  }
  .divider {
    width: 1px;
    height: 60px;
    background: var(--rule);
  }
  .contact-list {
    list-style: none;
    font-family: "Lato", sans-serif;
    font-size: 16px;
    color: var(--ink);
    line-height: 1.35;
    padding-top: 30px;
  }
  .contact-item {
    display: flex;
    align-items: center;
    gap: 9px;
  }
  .contact-icon { width: 12px; height: 12px; fill: var(--forest-ink); flex: none; }
</style>
</head>
<body>
<main class="canvas">
  <section class="card card-front" aria-label="Card front">
    <span class="brand-name">QUILLO</span>
  </section>

  <section class="card card-back" aria-label="Card back">
    <div class="identity">
      <p class="person-name">Daniel Reyes</p>
      <p class="person-title">Co-Founder &amp; CEO</p>
    </div>
    <div class="divider"></div>
    <ul class="contact-list">
      <li class="contact-item">
        <svg class="contact-icon" viewBox="0 0 12 12" aria-hidden="true"><path d="M1 3c0-1 1-2 2-2h6c1 0 2 1 2 2v1H8V3H4v1H1z"/><rect x="2" y="5" width="8" height="6" rx="1"/></svg>
        <span>+1 555-014-7026</span>
      </li>
      <li class="contact-item">
        <svg class="contact-icon" viewBox="0 0 12 12" aria-hidden="true"><path d="M0 2h12v1L6 7 0 3z"/><path d="M0 4.5l6 4 6-4V10H0z"/></svg>
        <span>team@quillo.com</span>
      </li>
      <li class="contact-item">
        <svg class="contact-icon" viewBox="0 0 12 12" aria-hidden="true"><circle cx="6" cy="6" r="5.5"/></svg>
        <span>www.quillo.com</span>
      </li>
    </ul>
  </section>
</main>
</body>
</html>
```